Letterhead/Envelope/Business Cards for law firm - Marlowe & Tesniere PLLC
Marlowe Tesniere
Letterhead/Envelope/Business Cards for law firm - Marlowe & Tesniere PLLC - Law
Creative Brief
Use same font as used in my logo
Open to any ideas
Simple
Doran P. Tesniere
Attorney
Marlowe & Tesniere PLLC 618 Briarmoss Court Plaza 375 North Galloway Avenue Louisville, Kentucky 40597
dtesniere@mtlegalgroup.example
www.mtlegalgroup.example
Licensed in Kentucky, Indiana & West Virginia
We are looking for design of letterhead, envelopes and business cards.
We want to use our logo. But we also need Marlowe & Tesniere, PLLC on the card/letterhead.

```html
<!DOCTYPE html>
<html lang="en">
<head>
<meta charset="utf-8">
<title>Marlowe &amp; Tesniere PLLC – Business Card</title>
<link rel="stylesheet" href="https://fonts.googleapis.com/css2?family=Cormorant+Garamond:wght@500&family=Open+Sans:wght@400;600;700&display=swap">
<style>
  :root {
    --backdrop: #2b2b2d;
    --red: #c8141c;
    --red-dark: #8f0a10;
    --red-light: #e0262c;
    --ink: #2a2a2a;
    --ink-soft: #555;
    --paper: #ffffff;
    --black: #111;
  }
  * { box-sizing: border-box; margin: 0; padding: 0; }
  html, body { width: 1200px; height: 874px; overflow: hidden; }
  body {
    background: var(--backdrop);
    font-family: "Open Sans", Arial, sans-serif;
    display: flex;
    align-items: center;
    justify-content: center;
    gap: 40px;
  }
  .card {
    width: 540px;
    height: 309px;
    border-radius: 16px;
    position: relative;
    overflow: hidden;
    box-shadow: 0 10px 30px rgba(0,0,0,.45);
  }
  .brand {
    display: flex;
    align-items: center;
    gap: 10px;
    font-family: "Cormorant Garamond", Georgia, serif;
    font-weight: 500;
    text-transform: uppercase;
    white-space: nowrap;
  }
  .brand-square { flex: none; }

  /* Front */
  .card-front {
    background: radial-gradient(circle at 50% 38%, var(--red-light) 0%, var(--red) 45%, var(--red-dark) 100%);
    color: var(--paper);
  }
  .card-front .brand {
    position: absolute;
    left: 50%; top: 118px;
    transform: translateX(-50%);
    font-size: 30px;
    letter-spacing: 4px;
  }
  .card-front .brand-square { width: 22px; height: 22px; background: var(--paper); }
  .front-web {
    position: absolute;
    left: 50%; top: 168px;
    transform: translateX(-50%);
    font-size: 11px;
    letter-spacing: 1px;
    opacity: .8;
  }

  /* Back */
  .card-back { background: var(--paper); color: var(--ink); }
  .card-back .brand {
    position: absolute;
    left: 30px; top: 104px;
    font-size: 21px;
    letter-spacing: 3px;
    color: var(--ink);
  }
  .card-back .brand-square { width: 18px; height: 18px; background: var(--red); }
  .name-band {
    position: absolute;
    left: 0; top: 148px;
    width: 300px; height: 32px;
    background: var(--red);
    border-radius: 0 16px 16px 0;
    color: var(--paper);
    display: flex; align-items: center;
    padding-left: 48px;
    font-size: 14px;
  }
  .name-band .person { font-weight: 600; }
  .name-band .role { font-size: 11px; margin-left: 10px; opacity: .9; }
  .band-tab {
    position: absolute;
    left: 0; top: 180px;
    width: 36px; height: 60px;
    background: var(--black);
  }
  .address {
    position: absolute;
    left: 48px; top: 194px;
    font-size: 12px;
    line-height: 17px;
    color: var(--ink);
  }
  .address .firm { font-weight: 700; }
  .contacts {
    position: absolute;
    right: 20px; top: 40px;
    list-style: none;
    font-size: 10px;
    line-height: 17px;
    color: var(--ink-soft);
  }
  .contacts li { display: flex; align-items: center; gap: 6px; }
  .contacts svg { width: 8px; height: 8px; fill: var(--red); flex: none; }
</style>
</head>
<body>
  <section class="card card-front" aria-label="Business card front">
    <div class="brand"><span class="brand-square"></span><span>Marlowe Tesniere</span></div>
    <div class="front-web">www.mtlegalgroup.example</div>
  </section>

  <section class="card card-back" aria-label="Business card back">
    <ul class="contacts">
      <li><svg viewBox="0 0 10 10"><path d="M2 0h2l1 3-1.5 1a6 6 0 0 0 2.5 2.5L7 5l3 1v2c0 1-1 2-2 2A8 8 0 0 1 0 2c0-1 1-2 2-2z"/></svg>502-555-0148</li>
      <li><svg viewBox="0 0 10 10"><rect x="1" y="3" width="8" height="5" rx="1"/><rect x="3" y="0" width="4" height="3"/></svg>502-555-0173</li>
      <li><svg viewBox="0 0 10 10"><rect x="2.5" y="0" width="5" height="10" rx="1"/></svg>502-555-0196</li>
      <li><svg viewBox="0 0 10 10"><path d="M0 2h10v6H0z"/></svg>dtesniere@mtlegalgroup.example</li>
      <li><svg viewBox="0 0 10 10"><circle cx="5" cy="5" r="5"/></svg>www.mtlegalgroup.example</li>
    </ul>

    <div class="brand"><span class="brand-square"></span><span>Marlowe Tesniere</span></div>

    <div class="name-band"><span class="person">Calvin Reyes</span><span class="role">President</span></div>
    <div class="band-tab"></div>

    <div class="address">
      <div class="firm">Marlowe &amp; Tesniere PLLC</div>
      <div>618 Briarmoss Court Plaza</div>
      <div>375 North Galloway Avenue</div>
      <div>Louisville, Kentucky 40597</div>
    </div>
  </section>
</body>
</html>
```